Business Card Design

I need a business card design for a new company based in Sydney called 'The Brisk Ladle'. We deliver organic, gourmet and fine foods to your door.

I would like to see creative, unique designs which use colours which represent health and nature like green.

Target Market(s)

Health conscious 20 to 35 year olds.

Industry/Entity Type

Health

Contact Information for Business Card

The Brisk Ladle, Owen Pardalis, owen@thebriskladle.com.au, 0427865193

Requirements
Must have
• My logo.

```html
<!DOCTYPE html>
<html lang="en">
<head>
<meta charset="utf-8">
<title>The Brisk Ladle — Business Card</title>
<link rel="stylesheet" href="https://fonts.googleapis.com/css2?family=Lato:wght@300;400&family=Marcellus&display=swap">
<style>
  :root {
    --front-top: #8b9f96;
    --front-bottom: #9aaca3;
    --back-center: #b9c8c1;
    --back-edge: #93a69d;
    --rule: rgba(110, 126, 118, 0.55);
    --seam: #c9d4cf;
    --brand-green: #a9c93a;
    --brand-dot: #7fa82a;
    --band: #3b3e3c;
    --name-ink: #d6dbd8;
    --name-edge: #1e201f;
    --contact-ink: #ffffff;
  }
  * { box-sizing: border-box; margin: 0; padding: 0; }
  html, body { width: 1062px; height: 1200px; overflow: hidden; background: #8b9f96; }
  .sheet { position: relative; width: 1062px; height: 1200px; }

  .card { position: absolute; left: 0; width: 1062px; overflow: hidden; }
  .card--front {
    top: 0; height: 594px;
    background: linear-gradient(180deg, var(--front-top), var(--front-bottom));
  }
  .card--back {
    top: 598px; height: 602px;
    background: radial-gradient(ellipse at 45% 35%, var(--back-center), var(--back-edge));
  }
  .seam { position: absolute; top: 594px; left: 0; width: 1062px; height: 4px; background: var(--seam); }

  .rule { position: absolute; height: 4px; background: var(--rule); border-radius: 2px; }

  .brand { position: absolute; display: flex; align-items: center; }
  .brand__dot { border-radius: 50%; background: var(--brand-dot); flex: none; }
  .brand__name {
    font-family: "Lato", sans-serif; font-weight: 300;
    color: var(--brand-green); line-height: 0.95;
  }

  .brand--front { left: 214px; top: 180px; }
  .brand--front .brand__dot { width: 186px; height: 186px; margin-right: 50px; }
  .brand--front .brand__name { font-size: 100px; }

  .brand--faint { left: 172px; top: 70px; opacity: 0.3; }
  .brand--faint .brand__dot { width: 176px; height: 176px; margin-right: 46px; }
  .brand--faint .brand__name { font-size: 94px; }

  .name-band {
    position: absolute; left: 0; top: 333px; width: 1062px; height: 98px;
    background: var(--band);
    display: flex; align-items: center; justify-content: center;
  }
  .name-band__name {
    font-family: "Marcellus", serif; font-size: 46px; letter-spacing: 2px;
    color: var(--name-ink); margin-left: 36px;
    -webkit-text-stroke: 1px var(--name-edge);
  }
  .contact { position: absolute; left: 0; width: 1062px; text-align: center; font-family: "Lato", sans-serif; color: var(--contact-ink); }
  .contact--email { top: 460px; font-size: 37px; padding-left: 60px; }
  .contact--phone { top: 532px; font-size: 28px; padding-right: 80px; }
</style>
</head>
<body>
<main class="sheet">
  <section class="card card--front">
    <div class="rule" style="top:28px;left:150px;width:760px"></div>
    <div class="rule" style="top:66px;left:40px;width:1000px"></div>
    <div class="rule" style="top:100px;left:80px;width:980px"></div>
    <div class="rule" style="top:138px;left:20px;width:920px"></div>

    <div class="brand brand--front">
      <span class="brand__dot"></span>
      <span class="brand__name">The Brisk<br>Ladle</span>
    </div>

    <div class="rule" style="top:444px;left:60px;width:890px"></div>
    <div class="rule" style="top:490px;left:130px;width:800px"></div>
    <div class="rule" style="top:520px;left:20px;width:1000px"></div>
    <div class="rule" style="top:556px;left:100px;width:840px"></div>
  </section>

  <div class="seam"></div>

  <section class="card card--back">
    <div class="brand brand--faint" aria-hidden="true">
      <span class="brand__dot"></span>
      <span class="brand__name">The Brisk<br>Ladle</span>
    </div>

    <div class="name-band">
      <h1 class="name-band__name">OWEN PARDALIS</h1>
    </div>

    <p class="contact contact--email">owen@thebriskladle.com.au</p>
    <p class="contact contact--phone">0427865193</p>
  </section>
</main>
</body>
</html>
```